Valmo Sàrl - Business Card

VALMO Sàrl operates in the sector Services for banks and credit institutions. It is a B2B which connects companies. The main colors should be Blue and Black. The logo and look of the card should be simple, professional, conservative and reflect Connecting People.

Target Market(s)

Financial professionals and institutions

Industry/Entity Type

Finance

Contact Information for Business Card

Chemin des Vergers 9
1026 Denges

Logo Text

Connecting dots

Font styles to use
Serif
Sans Serif

Colors
0355a3
3176b5
85acd3
cfdeed

Requirements
Should not have
• Multiple colors

```html
<!DOCTYPE html>
<html lang="en">
<head>
<meta charset="UTF-8">
<title>Valmo Sàrl – Business Card</title>
<link href="https://fonts.googleapis.com/css2?family=Open+Sans:wght@400;600;700&display=swap" rel="stylesheet">
<style>
  :root {
    --backdrop: #e9ebee;
    --card: #ffffff;
    --ink: #1d1d1f;
    --blue: #3ba3dc;
    --rule: #1d1d1f;
  }
  * { margin: 0; padding: 0; box-sizing: border-box; }
  html, body {
    width: 1200px; height: 1000px; overflow: hidden;
    background: var(--backdrop);
    font-family: "Open Sans", Arial, sans-serif;
    color: var(--ink);
  }
  .canvas { position: relative; width: 1200px; height: 1000px; }
  .card {
    position: absolute;
    width: 665px; height: 396px;
    background: var(--card);
    border-radius: 24px;
    box-shadow: 0 2px 6px rgba(0,0,0,0.12);
  }
  .card--front { left: 263px; top: 75px; }
  .card--back { left: 266px; top: 534px; }

  .wordmark {
    position: absolute;
    display: flex; align-items: center; gap: 12px;
    font-weight: 700; color: var(--ink);
    letter-spacing: -0.5px; white-space: nowrap;
  }
  .wordmark__dot { border-radius: 50%; background: var(--blue); flex: none; }
  .card--front .wordmark { left: 52px; top: 70px; font-size: 44px; }
  .card--front .wordmark__dot { width: 26px; height: 26px; }
  .card--back .wordmark { left: 0; right: 0; top: 140px; justify-content: center; font-size: 58px; }
  .card--back .wordmark__dot { width: 34px; height: 34px; }

  .holder { position: absolute; right: 44px; top: 176px; text-align: right; }
  .holder__name { font-size: 20px; font-weight: 600; line-height: 28px; }
  .holder__role { font-size: 16px; color: var(--blue); line-height: 24px; }

  .divider {
    position: absolute; left: 44px; right: 44px; top: 242px;
    height: 2px; background: var(--rule);
  }

  .contacts { position: absolute; left: 44px; top: 258px; list-style: none; }
  .contacts li {
    display: flex; align-items: center; gap: 6px;
    font-size: 17px; line-height: 24.5px; white-space: nowrap;
  }
  .contacts svg { width: 16px; height: 16px; fill: var(--blue); flex: none; }

  .address {
    position: absolute; right: 44px; top: 307px;
    text-align: right; font-size: 17px; line-height: 24.5px; font-style: normal;
    white-space: nowrap;
  }

  .site {
    position: absolute; left: 0; right: 0; top: 338px;
    text-align: center; font-size: 17px; letter-spacing: 1.2px;
  }
</style>
</head>
<body>
<div class="canvas">

  <section class="card card--front" aria-label="Card front">
    <div class="wordmark"><span class="wordmark__dot"></span>Valmo Sàrl</div>

    <div class="holder">
      <p class="holder__name">Daniel Marchetti</p>
      <p class="holder__role">CEO / Owner</p>
    </div>

    <div class="divider"></div>

    <ul class="contacts">
      <li>
        <svg viewBox="0 0 16 16" aria-hidden="true"><path d="M1 6c0-2 3-3.5 7-3.5S15 4 15 6v1.5h-3.5V6h-7v1.5H1z"/><path d="M3.5 8.5h9l1.5 5H2z"/></svg>
        021 555 01 42
      </li>
      <li>
        <svg viewBox="0 0 16 16" aria-hidden="true"><path d="M1 6c0-2 3-3.5 7-3.5S15 4 15 6v1.5h-3.5V6h-7v1.5H1z"/><path d="M3.5 8.5h9l1.5 5H2z"/></svg>
        021 555 01 42 EXT 21
      </li>
      <li>
        <svg viewBox="0 0 16 16" aria-hidden="true"><path d="M1 3.5h14v9H1z" fill="none" stroke="#3ba3dc" stroke-width="1.4"/><path d="M1 3.5l7 5.5 7-5.5" fill="none" stroke="#3ba3dc" stroke-width="1.4"/></svg>
        info@valmosarl.ch
      </li>
      <li>
        <svg viewBox="0 0 16 16" aria-hidden="true"><circle cx="7.5" cy="7.5" r="6" fill="none" stroke="#3ba3dc" stroke-width="1.5"/><path d="M1.5 7.5h12M7.5 1.5c-3 3.5-3 8.5 0 12M7.5 1.5c3 3.5 3 8.5 0 12" fill="none" stroke="#3ba3dc" stroke-width="1.1"/></svg>
        www.valmosarl.ch
      </li>
    </ul>

    <address class="address">
      Chemin des Vergers 9<br>
      1026 Denges
    </address>
  </section>

  <section class="card card--back" aria-label="Card back">
    <div class="wordmark"><span class="wordmark__dot"></span>Valmo Sàrl</div>
    <p class="site">www.valmosarl.ch</p>
  </section>

</div>
</body>
</html>
```